Vitamin Business Needs a Label Design

Hello. We are high-quality/healthy vitamin/supplement company, and we are in need of a Label design for a vitamin bottle.
Bottle will be either white or brown color. Label size will be 74mm*220mm. Please pick one logo from the attachments(you may use new design for the logo if you'd like to). On the front, please put two icon graphics(like certified organic sticker on food products) for "Kosher Certified" and "Vegetable Capsules". I attached sample of icon for your reference. I'm attaching files for the information. I will also put some example label designs on the brief page. Please let me know if you have any question. Thank you so much for the works!

Font styles to use
Serif
Sans Serif

Requirements
Must have
• Information on the files. I may put barcode later, so if possible, please leave a space for barcode. Thank you.
Nice to have
• White or Ivory color for the label background would be nice. But you may use different color if you'd like to. For your information, I prefer logo 2 over logo 1, but you can use any logo as long as the design looks great.
Should not have
• Please do not use sample icon or use icon from online. It is because there may be copyright issues. For color, please do not use dark colors for label background color. (if it looks very good, then its okay).

```html
<!DOCTYPE html>
<html lang="en">
<head>
<meta charset="utf-8">
<title>Verolin Multivitamin Labels</title>
<link href="https://fonts.googleapis.com/css2?family=Montserrat:wght@700;800&family=Open+Sans:ital,wght@0,400;0,600;1,700&display=swap" rel="stylesheet">
<style>
  :root {
    --page: #ececec;
    --label: #ffffff;
    --ink: #1a1a1a;
    --brand-ink: #3a3a3a;
    --grey: #5a5a5a;
    --green: #5ba52e;
    --blue: #2b8fd6;
  }
  html, body {
    margin: 0;
    padding: 0;
    width: 1200px;
    height: 1058px;
    overflow: hidden;
    background: var(--page);
  }
  .canvas {
    position: relative;
    width: 1200px;
    height: 1058px;
  }
  .label {
    --accent: var(--green);
    position: absolute;
    top: 249px;
    width: 520px;
    height: 560px;
    background: var(--label);
    box-shadow: 0 2px 10px rgba(0,0,0,0.12);
    overflow: hidden;
    font-family: "Open Sans", Arial, sans-serif;
    color: var(--ink);
  }
  .label--green { left: 60px; --accent: var(--green); }
  .label--blue { left: 620px; --accent: var(--blue); }

  .label__stripe {
    position: absolute;
    top: 0; left: 0;
    width: 100%;
    height: 16px;
    background: var(--accent);
  }
  .label__brand {
    position: absolute;
    top: 50px; left: 0;
    width: 100%;
    text-align: center;
    font-size: 54px;
    line-height: 74px;
    font-weight: 400;
    color: var(--brand-ink);
    letter-spacing: -0.5px;
  }
  .label__title {
    position: absolute;
    top: 162px; left: 0;
    width: 100%;
    text-align: center;
    font-family: "Montserrat", Arial, sans-serif;
    font-weight: 800;
    font-size: 58px;
    line-height: 1;
    color: var(--ink);
  }
  .label__title-accent { color: var(--accent); }
  .label__subtitle {
    position: absolute;
    top: 220px; left: 0;
    width: 100%;
    text-align: center;
    font-family: "Montserrat", Arial, sans-serif;
    font-weight: 700;
    font-size: 30px;
    letter-spacing: 3px;
    line-height: 1;
    color: var(--grey);
  }
  .label__kind {
    position: absolute;
    top: 250px; left: 0;
    width: 100%;
    text-align: center;
    font-size: 18px;
    line-height: 20px;
    letter-spacing: 1px;
    color: var(--grey);
  }
  .support {
    position: absolute;
    top: 324px; left: 102px;
  }
  .support__bracket {
    position: absolute;
    top: 10px; left: 0;
    width: 10px;
    height: 132px;
    border: 2px solid var(--ink);
    border-right: none;
  }
  .support__heading {
    position: absolute;
    top: 0; left: 22px;
    white-space: nowrap;
    font-size: 23px;
    line-height: 30px;
    font-style: italic;
    font-weight: 700;
  }
  .support__list {
    position: absolute;
    top: 31px; left: 22px;
    margin: 0; padding: 0;
    list-style: none;
    font-size: 24px;
    line-height: 28px;
    white-space: nowrap;
  }
  .support__item--accent { color: var(--accent); }
  .badge {
    position: absolute;
    top: 340px; left: 422px;
    width: 74px; height: 74px;
  }
  .band {
    position: absolute;
    top: 490px; left: 0;
    width: 410px;
    height: 42px;
    background: var(--accent);
    clip-path: polygon(0 0, 100% 0, 94% 100%, 0 100%);
    color: #fff;
    font-size: 22px;
    line-height: 42px;
    padding-left: 40px;
    box-sizing: border-box;
  }
  .count {
    position: absolute;
    top: 458px; left: 424px;
    width: 68px; height: 54px;
    background: var(--ink);
    color: #fff;
    text-align: center;
  }
  .count__number {
    display: block;
    font-family: "Montserrat", Arial, sans-serif;
    font-weight: 800;
    font-size: 26px;
    line-height: 1;
    padding-top: 8px;
  }
  .count__unit {
    display: block;
    font-size: 9px;
    font-weight: 600;
    letter-spacing: 0.5px;
    margin-top: 3px;
  }
</style>
</head>
<body>
<main class="canvas">

  <section class="label label--green">
    <div class="label__stripe"></div>
    <div class="label__brand">Verolin</div>
    <div class="label__title">MULTI<span class="label__title-accent">VITAMIN</span></div>
    <div class="label__subtitle">MULTIMINERAL</div>
    <div class="label__kind">SUPPLEMENT</div>
    <div class="support">
      <div class="support__bracket"></div>
      <div class="support__heading">Essential support for:</div>
      <ul class="support__list">
        <li>Overall Health</li>
        <li class="support__item--accent">Immune System</li>
        <li>Energy</li>
        <li class="support__item--accent">Metabolism</li>
      </ul>
    </div>
    <svg class="badge" viewBox="0 0 74 74" role="img" aria-label="Certification badge">
      <circle cx="37" cy="37" r="36" fill="#ffffff" stroke="#1a1a1a" stroke-width="2"/>
      <circle cx="37" cy="37" r="31" fill="#1a1a1a"/>
      <rect x="8" y="30" width="58" height="14" fill="#ffffff"/>
      <rect x="10" y="32" width="54" height="10" fill="#1a1a1a"/>
    </svg>
    <div class="band">Dietary Supplement</div>
    <div class="count"><span class="count__number">180</span><span class="count__unit">CAPSULES</span></div>
  </section>

  <section class="label label--blue">
    <div class="label__stripe"></div>
    <div class="label__brand">Verolin</div>
    <div class="label__title">MULTI<span class="label__title-accent">VITAMIN</span></div>
    <div class="label__subtitle">MULTIMINERAL</div>
    <div class="label__kind">SUPPLEMENT</div>
    <div class="support">
      <div class="support__bracket"></div>
      <div class="support__heading">Essential support for:</div>
      <ul class="support__list">
        <li>Overall Health</li>
        <li class="support__item--accent">Immune System</li>
        <li>Energy</li>
        <li class="support__item--accent">Metabolism</li>
      </ul>
    </div>
    <svg class="badge" viewBox="0 0 74 74" role="img" aria-label="Certification badge">
      <circle cx="37" cy="37" r="36" fill="#ffffff" stroke="#1a1a1a" stroke-width="2"/>
      <circle cx="37" cy="37" r="31" fill="#1a1a1a"/>
      <rect x="8" y="30" width="58" height="14" fill="#ffffff"/>
      <rect x="10" y="32" width="54" height="10" fill="#1a1a1a"/>
    </svg>
    <div class="band">Dietary Supplement</div>
    <div class="count"><span class="count__number">180</span><span class="count__unit">CAPSULES</span></div>
  </section>

</main>
</body>
</html>
```